Risk Management Company in need of Business Card Design

We sell risk management insurance to Lenders (Banks, Credit Unions, Real Estate Trust).

We need a very clean, professional card that will leave a great impression.

We are looking to use a blue color for our logo on the card (Preferably close to royal blue but are open to looking at navy blue or any darker blues as well).

Please see the logo attached to get an idea. We are open to writing Harbor Shield Under the logo or next to the logo. Really whatever looks best.

Target Market(s)

Banks, Credit Unions, Real Estate Trusts

Industry/Entity Type

Insurance

Contact Information for Business Card

Name: Mark Dunstan
Title: Regional Sales Director
Email: mdunstan@harborshield.example
C:410-555-0143
D:410-555-0187
888-555-0129 Ext.318
F:443-555-0164 (We would like to see some cards without the fax number as well to compare)

Company Name: Harbor Shield
Website: www.harborshield.example

Address: 118 E. Morrow St. Suite 420, Ashford, MD 21299 (Preferably written on the bottom of the card in small print.)

Colors
0355a3
0455a3

Requirements
Nice to have
• We would like to see a couple of where the back has the logo in reverse colors (Logo White, Background Blue)

```html
<!DOCTYPE html>
<html lang="en">
<head>
<meta charset="utf-8">
<title>Harbor Shield — Business Card</title>
<link href="https://fonts.googleapis.com/css2?family=Rokkitt:wght@400;500;600&display=swap" rel="stylesheet">
<style>
  :root {
    --ink-blue: #1f3a93;
    --charcoal: #2f2f31;
    --steel: #8a8a8e;
    --text-grey: #7d7d80;
    --paper: #ffffff;
    --backdrop: #e8e8e9;
  }
  * { box-sizing: border-box; margin: 0; padding: 0; }
  html, body { width: 1200px; height: 1000px; overflow: hidden; }
  body {
    background: var(--backdrop);
    font-family: "Rokkitt", Georgia, serif;
    position: relative;
  }
  .card {
    position: absolute;
    left: 250px;
    width: 700px;
    height: 400px;
    background: var(--paper);
    box-shadow: 0 6px 18px rgba(0,0,0,0.18);
    overflow: hidden;
  }
  .card--front { top: 70px; }
  .card--back { top: 530px; }

  .front-shapes { position: absolute; inset: 0; }

  .brand {
    position: absolute;
    left: 205px;
    top: 34px;
  }
  .brand__name {
    font-size: 36px;
    font-weight: 500;
    color: var(--ink-blue);
    text-transform: uppercase;
    letter-spacing: 2px;
    line-height: 1;
  }
  .brand__tagline {
    font-size: 12px;
    color: var(--text-grey);
    text-transform: uppercase;
    letter-spacing: 1.4px;
    margin-top: 3px;
  }
  .person {
    position: absolute;
    left: 232px;
    top: 100px;
  }
  .person__name {
    font-size: 30px;
    font-weight: 600;
    color: var(--ink-blue);
    line-height: 1;
  }
  .person__title {
    font-size: 14px;
    color: var(--text-grey);
    margin-top: 2px;
  }
  .contacts {
    position: absolute;
    left: 232px;
    top: 170px;
    list-style: none;
  }
  .contacts__row {
    display: flex;
    align-items: center;
    height: 32px;
    font-size: 21px;
    color: var(--charcoal);
  }
  .contacts__key {
    width: 24px;
    height: 24px;
    background: var(--ink-blue);
    color: var(--paper);
    font-size: 16px;
    font-weight: 600;
    display: flex;
    align-items: center;
    justify-content: center;
    margin-right: 12px;
  }
  .contacts__ext { font-size: 14px; color: var(--text-grey); margin-left: 3px; }
  .contacts__gap { margin-left: 12px; }
  .address {
    position: absolute;
    left: 232px;
    top: 318px;
    font-size: 16px;
    font-style: normal;
    color: var(--text-grey);
    line-height: 1.35;
  }

  .back-shapes { position: absolute; inset: 0; }
  .website {
    position: absolute;
    left: 0;
    top: 0;
    width: 44px;
    height: 400px;
    display: flex;
    align-items: center;
    justify-content: center;
    writing-mode: vertical-rl;
    transform: rotate(180deg);
    color: var(--paper);
    font-size: 17px;
    font-weight: 600;
    letter-spacing: 1px;
  }
  .back-brand {
    position: absolute;
    left: 150px;
    top: 150px;
    height: 100px;
    display: flex;
    align-items: center;
    gap: 22px;
  }
  .back-brand__dot {
    width: 44px;
    height: 44px;
    border-radius: 50%;
    background: var(--ink-blue);
  }
  .back-brand__name {
    font-size: 52px;
    font-weight: 500;
    color: var(--ink-blue);
    text-transform: uppercase;
    letter-spacing: 3px;
  }
</style>
</head>
<body>
  <section class="card card--front">
    <svg class="front-shapes" width="700" height="400" viewBox="0 0 700 400">
      <path d="M0 40 H170 V108 A42 42 0 0 1 128 150 H0 Z" fill="var(--ink-blue)"/>
      <path d="M60 168 H170 V400 H60 Z" fill="var(--ink-blue)"/>
    </svg>
    <div class="brand">
      <div class="brand__name">Harbor Shield</div>
      <div class="brand__tagline">Risk Management Insurance Company</div>
    </div>
    <div class="person">
      <div class="person__name">Mark Dunstan</div>
      <div class="person__title">Regional Sales Director</div>
    </div>
    <ul class="contacts">
      <li class="contacts__row"><span class="contacts__key">E</span>mdunstan@harborshield.example</li>
      <li class="contacts__row"><span class="contacts__key">C</span>410-555-0143</li>
      <li class="contacts__row"><span class="contacts__key">D</span>410-555-0187<span class="contacts__gap">888-555-0129</span><span class="contacts__ext">Ext.318</span></li>
      <li class="contacts__row"><span class="contacts__key">F</span>443-555-0164</li>
    </ul>
    <address class="address">
      118 E. Morrow St. Suite 420,<br>Ashford, MD 21299
    </address>
  </section>

  <section class="card card--back">
    <svg class="back-shapes" width="700" height="400" viewBox="0 0 700 400">
      <rect x="0" y="0" width="44" height="400" fill="var(--charcoal)"/>
      <rect x="44" y="0" width="10" height="400" fill="var(--steel)"/>
      <rect x="120" y="32" width="580" height="112" fill="var(--ink-blue)"/>
      <rect x="86" y="256" width="614" height="112" fill="var(--ink-blue)"/>
    </svg>
    <div class="website">www.harborshield.example</div>
    <div class="back-brand">
      <span class="back-brand__dot"></span>
      <span class="back-brand__name">Harbor Shield</span>
    </div>
  </section>
</body>
</html>
```